Tallow Accounting Business Card design

We need a stand out business card design for Accounting practice based in Australia specialising in pubs, clubs and hotels. We help venues maximise margins, create time and manage cashflow. One club we have been working with for the last 6 months has increased revenue by 3% and margin by 5% in this time frame. We have a back office outsourced system that costs less than having a full time employee and also allows the venues the added benefit of:<br/>-using the office space to become a revenue generating opportunity. <br/>-a complete system to enhance governance, accountability and efficiency within their operation<br/>-52 weeks cover so no hassle to cover annual/sick .. leave<br/><br/>We would like to see designs that use the colours of our logo (green & blue).
Target Market(s)
Australian Pubs, Clubs & Hotels abookkeeping, accounting and tax services
Industry/Entity Type
Accountant
Contact Information for Business Card
Miriel Dawkes CPA
Principal
Accountant Tax Agent
Miriel@TallowAccounting.example.au
0418639174
www.tallowaccounting.example.au
Accounting / Payroll / Tax / SMSF / Technology
Colors
Designer to choose colors to be used in the design.
Look and feel
Each slider illustrates characteristics of the customer's brand and the style your logo design should communicate.

```html
<!DOCTYPE html>
<html lang="en">
<head>
<meta charset="utf-8">
<title>Tallow Accounting Business Card</title>
<link rel="stylesheet" href="https://fonts.googleapis.com/css2?family=Roboto:wght@400;500;700&display=swap">
<style>
  :root {
    --page: #e8e4df;
    --card: #111111;
    --blue: #2b4a9f;
    --green: #1f7a40;
    --text: #e9e9e9;
  }
  * { box-sizing: border-box; margin: 0; padding: 0; }
  html, body { width: 1200px; height: 1200px; overflow: hidden; }
  body {
    background: var(--page);
    font-family: "Roboto", Arial, sans-serif;
    position: relative;
  }
  .card {
    position: absolute;
    left: 214px;
    width: 772px;
    height: 442px;
    background: var(--card);
    box-shadow: 0 6px 18px rgba(0,0,0,0.25);
  }
  .card--front { top: 150px; }
  .card--back { top: 634px; }

  .brand {
    position: absolute;
    display: flex;
    align-items: center;
    gap: 14px;
  }
  .brand__dot {
    border-radius: 50%;
    border: 3px solid var(--green);
    flex: none;
  }
  .brand__name {
    color: var(--blue);
    font-weight: 700;
    white-space: nowrap;
    line-height: 1;
  }
  .card--front .brand { left: 36px; top: 200px; }
  .card--front .brand__dot { width: 44px; height: 44px; }
  .card--front .brand__name { font-size: 29px; }

  .divider {
    position: absolute;
    left: 386px;
    top: 132px;
    width: 2px;
    height: 182px;
    background: var(--green);
  }
  .contact {
    position: absolute;
    left: 421px;
    top: 128px;
    color: var(--text);
  }
  .contact__name {
    font-size: 25px;
    font-weight: 500;
    color: var(--blue);
    line-height: 1.2;
  }
  .contact__name .credential { color: var(--green); font-weight: 400; }
  .contact__role {
    font-size: 19px;
    line-height: 25px;
    margin-top: 4px;
  }
  .contact__list { list-style: none; margin-top: 24px; }
  .contact__list li {
    display: flex;
    align-items: center;
    gap: 9px;
    font-size: 17.5px;
    line-height: 27px;
  }
  .contact__list svg { width: 15px; height: 15px; fill: var(--blue); flex: none; }

  .card--back .brand {
    left: 0; right: 0; top: 178px;
    justify-content: center;
    gap: 20px;
  }
  .card--back .brand__dot { width: 70px; height: 70px; border-width: 4px; }
  .card--back .brand__name { font-size: 50px; }

  .services {
    position: absolute;
    left: 0; right: 0;
    top: 385px;
    text-align: center;
    font-size: 18px;
    color: var(--blue);
  }
  .services .sep { color: var(--green); margin: 0 9px; font-size: 14px; }
</style>
</head>
<body>
  <section class="card card--front">
    <div class="brand">
      <span class="brand__dot"></span>
      <span class="brand__name">Tallow Accounting</span>
    </div>
    <div class="divider"></div>
    <div class="contact">
      <h1 class="contact__name">Miriel Dawkes <span class="credential">CPA</span></h1>
      <p class="contact__role">Principal<br>Accountant Tax Agent</p>
      <ul class="contact__list">
        <li>
          <svg viewBox="0 0 24 24" aria-hidden="true"><path d="M6.6 10.8a15.1 15.1 0 0 0 6.6 6.6l2.2-2.2a1 1 0 0 1 1-.25 11.4 11.4 0 0 0 3.6.57 1 1 0 0 1 1 1V20a1 1 0 0 1-1 1A17 17 0 0 1 3 4a1 1 0 0 1 1-1h3.5a1 1 0 0 1 1 1c0 1.25.2 2.45.57 3.57a1 1 0 0 1-.25 1z"/></svg>
          0418 639 174
        </li>
        <li>
          <svg viewBox="0 0 24 24" aria-hidden="true"><path d="M2 5h20v14H2z M3 6l9 7 9-7" fill="none" stroke="#2b4a9f" stroke-width="0"/><path d="M2 5h20v2l-10 7L2 7z M2 9l10 7 10-7v10H2z"/></svg>
          Miriel@TallowAccounting.example.au
        </li>
        <li>
          <svg viewBox="0 0 24 24" aria-hidden="true"><path d="M12 2a10 10 0 1 0 0 20 10 10 0 0 0 0-20zm6.9 6h-2.9a15.6 15.6 0 0 0-1.4-3.6A8 8 0 0 1 18.9 8zM12 4c.8 1.2 1.5 2.5 1.9 4h-3.8c.4-1.5 1.1-2.8 1.9-4zM4.3 14a8.2 8.2 0 0 1 0-4h3.4a16.5 16.5 0 0 0 0 4zm.8 2h2.9c.3 1.3.8 2.5 1.4 3.6A8 8 0 0 1 5.1 16zM8 8H5.1a8 8 0 0 1 4.3-3.6C8.8 5.5 8.3 6.7 8 8zm4 12c-.8-1.2-1.5-2.5-1.9-4h3.8c-.4 1.5-1.1 2.8-1.9 4zm2.3-6H9.7a14.7 14.7 0 0 1 0-4h4.6a14.7 14.7 0 0 1 0 4zm.3 5.6c.6-1.1 1.1-2.3 1.4-3.6h2.9a8 8 0 0 1-4.3 3.6zm1.7-5.6a16.5 16.5 0 0 0 0-4h3.4a8.2 8.2 0 0 1 0 4z"/></svg>
          www.tallowaccounting.example.au
        </li>
      </ul>
    </div>
  </section>

  <section class="card card--back">
    <div class="brand">
      <span class="brand__dot"></span>
      <span class="brand__name">Tallow Accounting</span>
    </div>
    <p class="services">
      Accounting<span class="sep">•</span>Payroll<span class="sep">•</span>Tax<span class="sep">•</span>SMSF<span class="sep">•</span>Technology
    </p>
  </section>
</body>
</html>
```